Upsell Vertical Banner Ad Design For B2B Marketing Agency Vertical 768px × 1180px IS THE SIZE

I need a banner made for my website www.brightlanepromotionhub.biz This banner will be an upsell advertisement for after someone signs up for my monthly program. When they login to their account for the 1st time I will give them the chance to upgrade their account to our annual program with just one click.

this is a page that upsells it currently to give you an idea how we market ourselves:
https://tlpx.pagevault-example.com/page/tlp-annual-upsell

Use this content:

Are You Ready To Commit To Taking Your Business To The Next Level?

Because We're In This For The Long-Haul and Dedicated To Your Success...

Save $300 By Upgrading To An Annual Membership And Pay Only $74/mth

((BUTTON))Yes, Upgrade My Plan Right Now!

*Must prepay the full year at only $898/yr!

Target Market(s)

business owners

Industry/Entity Type

Marketing

Requirements
Must have
• 768px × 1180px IS THE SIZE vertical

Use this content:

Nice to have
• Use this content:

Should not have
• Use this content:

```html
<!DOCTYPE html>
<html lang="en">
<head>
<meta charset="UTF-8">
<title>Bright Lane Promotion Hub – Annual Upgrade Banner</title>
<link href="https://fonts.googleapis.com/css2?family=Roboto:wght@400;500;700&display=swap" rel="stylesheet">
<style>
  :root {
    --bg: #e8f2fc;
    --wave: #0b9be6;
    --wave-light: #ffffff;
    --heading: #55575a;
    --accent: #1b6db3;
    --button: #0ea0ea;
    --button-shadow: rgba(14, 120, 200, 0.28);
    --white: #ffffff;
    --art-top: #d6e9fa;
    --art-bottom: #bcdcf6;
  }
  * { box-sizing: border-box; margin: 0; padding: 0; }
  html, body { width: 781px; height: 1200px; overflow: hidden; background: var(--bg); }
  .banner {
    position: relative;
    width: 781px;
    height: 1200px;
    overflow: hidden;
    background: var(--bg);
    font-family: "Roboto", Arial, sans-serif;
  }
  .waves { position: absolute; inset: 0; width: 781px; height: 1200px; }
  .brand {
    position: absolute;
    left: 54px;
    top: 30px;
    display: flex;
    align-items: center;
    gap: 10px;
  }
  .brand-dot {
    width: 30px; height: 30px;
    border-radius: 50%;
    background: var(--accent);
  }
  .brand-name {
    font-size: 21px;
    font-weight: 700;
    color: var(--accent);
    letter-spacing: 0.5px;
    text-transform: uppercase;
  }
  .headline {
    position: absolute;
    top: 155px;
    left: 0; right: 0;
    text-align: center;
    color: var(--heading);
    font-size: 34px;
    font-weight: 500;
    line-height: 41px;
  }
  .subline {
    position: absolute;
    top: 258px;
    left: 0; right: 0;
    text-align: center;
    color: var(--heading);
    font-size: 25px;
    font-weight: 400;
    line-height: 34px;
  }
  .offer {
    position: absolute;
    top: 364px;
    left: 0; right: 0;
    text-align: center;
    color: var(--accent);
    font-size: 33px;
    font-weight: 400;
    line-height: 44px;
  }
  .offer-lead { font-size: 41px; }
  .cta {
    position: absolute;
    left: 102px;
    top: 575px;
    width: 574px;
    height: 72px;
    border-radius: 6px;
    background: var(--button);
    box-shadow: 0 4px 14px var(--button-shadow);
    color: var(--white);
    font-size: 28px;
    font-weight: 500;
    display: flex;
    align-items: center;
    justify-content: center;
    text-decoration: none;
  }
  .growth-art {
    position: absolute;
    left: 110px;
    top: 660px;
    width: 590px;
    height: 370px;
    border-radius: 18px;
    background: linear-gradient(180deg, var(--art-top), var(--art-bottom));
  }
  .terms {
    position: absolute;
    left: 42px;
    top: 1106px;
    color: var(--white);
    font-size: 28px;
    font-weight: 400;
  }
</style>
</head>
<body>
  <div class="banner">
    <svg class="waves" viewBox="0 0 781 1200" aria-hidden="true">
      <path d="M470 0 C560 45 690 70 781 58 L781 0 Z" fill="var(--wave)"/>
      <path d="M0 1060 C200 1010 330 1100 520 1085 C640 1075 720 1040 781 1030 L781 1200 L0 1200 Z" fill="var(--wave-light)"/>
      <path d="M0 1080 C210 1040 330 1115 520 1100 C640 1090 720 1060 781 1052 L781 1200 L0 1200 Z" fill="var(--wave)"/>
    </svg>

    <header class="brand">
      <span class="brand-dot"></span>
      <span class="brand-name">Bright Lane Promotion Hub</span>
    </header>

    <h1 class="headline">Are You Ready To Commit To Taking<br>Your Business To The Next Level?</h1>
    <p class="subline">Because We're In This For The Long-Haul<br>and Dedicated To Your Success...</p>
    <p class="offer"><span class="offer-lead">Save $300</span> By Upgrading To An<br>Annual Membership And Pay Only<br>$74/mth</p>

    <a class="cta" href="#">Yes, Upgrade My Plan Right Now!</a>

    <div class="growth-art" role="img" aria-label="Line-art illustration of a laptop showing a rising growth chart with a rocket, surrounded by icons of money bags, coins, clouds, gears, a clock, a phone, a magnifier and a light bulb"></div>

    <p class="terms">*Must prepay the full year at only $898/yr!</p>
  </div>
</body>
</html>
```